Creative Photography Business Card

Looking for a unique, creative, elegant, sophisticated and professional business card for my photography business.

I specialise in children, families, modelling, weddings and special event photography

Things to include:
Logo - will attach
Email: hello@mirenholtstudio.com.au
web:www.mirenholtstudio.com.au
Ph: 0438 561 204

I will also upload some of my work that you may like to use.

Please be creative and unique in your designs.

Reason: Currently away for work...finding it hard to give feedback in time for the deadline - sorry.

```html
<!DOCTYPE html>
<html lang="en">
<head>
<meta charset="utf-8">
<title>Miren Holt Studio – Business Card</title>
<link href="https://fonts.googleapis.com/css2?family=Lato:wght@300;400;700&display=swap" rel="stylesheet">
<style>
  :root {
    --backdrop: #3b3b3d;
    --card-black: #050505;
    --brand-blue: #2f6aa8;
    --text-light: #e9e9e9;
    --shadow: rgba(0, 0, 0, 0.45);
  }
  * { margin: 0; padding: 0; box-sizing: border-box; }
  html, body {
    width: 1200px;
    height: 926px;
    overflow: hidden;
    background: var(--backdrop);
    font-family: "Lato", sans-serif;
  }
  .sheet {
    position: relative;
    width: 1200px;
    height: 926px;
  }
  .card {
    position: absolute;
    left: 260px;
    width: 680px;
    height: 416px;
    overflow: hidden;
    box-shadow: 0 14px 30px var(--shadow);
  }
  .card--front { top: 27px; background: var(--card-black); }
  .card--back  { top: 483px; background: var(--card-black); }

  .collage { position: absolute; inset: 0; display: block; }

  .brand {
    position: absolute;
    display: flex;
    align-items: center;
    justify-content: center;
    border: 2px solid var(--brand-blue);
    border-radius: 50%;
    color: var(--brand-blue);
    font-family: "Lato", sans-serif;
    font-weight: 400;
    text-align: center;
    line-height: 1.05;
  }
  .brand--front {
    left: 38px;
    bottom: 26px;
    width: 104px;
    height: 104px;
    font-size: 19px;
  }
  .brand--back {
    left: 50%;
    top: 58px;
    transform: translateX(-50%);
    width: 156px;
    height: 156px;
    font-size: 28px;
  }

  .contact {
    position: absolute;
    top: 246px;
    left: 0;
    right: 0;
    color: var(--text-light);
    font-size: 17px;
    font-weight: 300;
    line-height: 1.55;
    text-align: center;
  }
  .contact__row { white-space: nowrap; }
  .contact__label { font-weight: 700; }
</style>
</head>
<body>
<main class="sheet">

  <section class="card card--front">
    <svg class="collage" viewBox="0 0 680 416" width="680" height="416">
      <defs>
        <linearGradient id="tone-child" x1="0" y1="0" x2="1" y2="1">
          <stop offset="0" stop-color="#e9c9a3"/><stop offset="1" stop-color="#9bc25a"/>
        </linearGradient>
        <linearGradient id="tone-wedding" x1="0" y1="0" x2="1" y2="1">
          <stop offset="0" stop-color="#6d8f4a"/><stop offset="0.5" stop-color="#c99479"/><stop offset="1" stop-color="#2d2b2c"/>
        </linearGradient>
        <linearGradient id="tone-family" x1="0" y1="0" x2="1" y2="1">
          <stop offset="0" stop-color="#7fa66b"/><stop offset="0.6" stop-color="#4d5868"/><stop offset="1" stop-color="#a9a39a"/>
        </linearGradient>
        <linearGradient id="tone-portrait" x1="0" y1="0" x2="1" y2="1">
          <stop offset="0" stop-color="#b8b3a8"/><stop offset="0.5" stop-color="#c99a7e"/><stop offset="1" stop-color="#6b4a36"/>
        </linearGradient>
        <linearGradient id="tone-kids" x1="0" y1="0" x2="1" y2="1">
          <stop offset="0" stop-color="#bdb9b0"/><stop offset="0.45" stop-color="#a6775a"/><stop offset="1" stop-color="#e08a4a"/>
        </linearGradient>
      </defs>
      <polygon role="img" aria-label="Photo of a smiling blonde child" fill="url(#tone-child)" points="0,0 110,0 0,152"/>
      <polygon role="img" aria-label="Wedding photo of a bride and groom kissing" fill="url(#tone-wedding)" points="110,0 250,0 0,347 0,152"/>
      <polygon role="img" aria-label="Outdoor family group photo" fill="url(#tone-family)" points="250,0 400,0 100,416 0,416 0,347"/>
      <polygon role="img" aria-label="Portrait of a young woman resting her chin on her hands" fill="url(#tone-portrait)" points="400,0 540,0 240,416 100,416"/>
      <polygon role="img" aria-label="Photo of a laughing boy in an orange shirt with a young girl" fill="url(#tone-kids)" points="540,0 680,0 680,416 240,416"/>
      <polygon class="corner-band" fill="var(--card-black)" points="0,200 0,416 320,416"/>
    </svg>
    <div class="brand brand--front">Miren<br>Holt</div>
  </section>

  <section class="card card--back">
    <div class="brand brand--back">Miren<br>Holt</div>
    <div class="contact">
      <p class="contact__row"><span class="contact__label">phone:</span> 0438 561 204</p>
      <p class="contact__row"><span class="contact__label">web:</span> www.mirenholtstudio.com.au</p>
      <p class="contact__row"><span class="contact__label">email:</span> hello@mirenholtstudio.com.au</p>
    </div>
  </section>

</main>
</body>
</html>
```